I need business cards for a company that will be an umbrella for many retail stores. I need them to be sleek and modern. I would like some white and black in the background of the card as these are the office colours the logo is attached.
Target Market(s)
worldwide
Industry/Entity Type
Business
Requirements
Must have
- traditional business card shape
Should not have
- too many colours
no swirly text

```html
<!DOCTYPE html>
<html lang="en">
<head>
<meta charset="utf-8">
<title>Navora General Trading – Business Card</title>
<link rel="stylesheet" href="https://fonts.googleapis.com/css2?family=Open+Sans:wght@400;600;700&display=swap">
<style>
  :root {
    --ink: #000000;
    --paper: #ffffff;
    --brand-blue: #0a6fb8;
    --pill-blue: #1a95d4;
    --rule-grey: #bdbdbd;
    --text-dark: #1a1a1a;
    --brand-grey: #6d6d6d;
    --stage: #ecebe8;
  }
  * { margin: 0; padding: 0; box-sizing: border-box; }
  html, body { width: 1200px; height: 900px; overflow: hidden; }
  body {
    background: var(--stage);
    font-family: "Open Sans", Arial, sans-serif;
    position: relative;
  }
  .card {
    position: absolute;
    width: 525px;
    height: 300px;
    background: var(--paper);
    overflow: hidden;
    box-shadow: 0 3px 10px rgba(0,0,0,0.18);
  }

  /* ---------- Front ---------- */
  .card--front { left: 495px; top: 125px; }
  .front__panel {
    position: absolute; left: 0; top: 0;
    width: 207px; height: 100%;
    background: var(--ink);
  }
  .front__rule {
    position: absolute; left: 0; width: 100%; height: 2px;
    background: var(--rule-grey);
  }
  .front__rule--top { top: 116px; }
  .front__rule--bottom { top: 157px; }
  .front__brand-bar {
    position: absolute; left: 211px; top: 13px;
    width: 7px; height: 62px;
    background: var(--brand-blue);
  }
  .front__brand {
    position: absolute; left: 236px; top: 34px;
    display: flex; align-items: center; gap: 8px;
    font-size: 13px; font-weight: 600; letter-spacing: 1.5px;
    color: var(--brand-grey);
  }
  .front__brand-dot {
    width: 12px; height: 12px; border-radius: 50%;
    background: var(--brand-blue);
  }
  .front__name {
    position: absolute; top: 118px; left: 0; width: 100%;
    height: 39px; line-height: 39px;
    font-size: 33px; font-weight: 600;
  }
  .front__first {
    position: absolute; right: 320px;
    color: var(--paper);
  }
  .front__last {
    position: absolute; left: 211px;
    color: var(--brand-blue);
  }
  .front__title {
    position: absolute; left: 211px; top: 166px;
    font-size: 14px; font-weight: 700; color: var(--text-dark);
  }
  .contact {
    position: absolute; left: 0; top: 191px;
    list-style: none;
  }
  .contact__row {
    display: flex; align-items: center;
    height: 24px; margin-bottom: 0.5px;
  }
  .contact__label {
    width: 207px; display: flex; justify-content: flex-end; padding-right: 4px;
  }
  .contact__pill {
    background: var(--pill-blue); color: var(--paper);
    font-size: 10.5px; letter-spacing: 0.3px;
    padding: 2px 10px; border-radius: 9px;
    line-height: 14px;
  }
  .contact__value {
    padding-left: 9px;
    font-size: 11px; color: var(--text-dark);
  }
  .front__tab {
    position: absolute; right: 0; bottom: 0;
    width: 138px; height: 8px;
    background: var(--brand-blue);
    border-top-left-radius: 14px;
  }

  /* ---------- Back ---------- */
  .card--back { left: 100px; top: 485px; }
  .back__panel {
    position: absolute; left: 367px; top: 0;
    width: 158px; height: 100%;
    background: var(--ink);
    border-top-left-radius: 32px;
    border-bottom-left-radius: 32px;
  }
  .back__bar {
    position: absolute; left: 40px; top: 116px;
    width: 7px; height: 86px;
    background: linear-gradient(to bottom, var(--brand-blue) 0%, var(--brand-blue) 40%, rgba(10,111,184,0) 100%);
  }
  .tagline {
    position: absolute; left: 58px;
    font-size: 13px; color: var(--text-dark);
    white-space: nowrap;
  }
  .tagline__accent { color: var(--pill-blue); }
  .tagline--main { top: 126px; }
  .tagline--reflection {
    top: 144px;
    transform: scaleY(-1);
    opacity: 0.75;
  }
  .back__brand {
    position: absolute; left: 320px; top: 56px;
    writing-mode: vertical-rl;
    display: flex; align-items: center; gap: 8px;
    font-size: 14px; font-weight: 600; letter-spacing: 1.5px;
    color: var(--brand-grey);
  }
  .back__brand-dot {
    width: 12px; height: 12px; border-radius: 50%;
    background: var(--brand-blue);
  }
</style>
</head>
<body>

<section class="card card--front" aria-label="Business card front">
  <div class="front__panel"></div>
  <div class="front__rule front__rule--top"></div>
  <div class="front__rule front__rule--bottom"></div>

  <div class="front__brand-bar"></div>
  <div class="front__brand">
    <span class="front__brand-dot"></span>
    <span>NAVORA GENERAL TRADING</span>
  </div>

  <h1 class="front__name">
    <span class="front__first">Martin</span>
    <span class="front__last">R. Delcove</span>
  </h1>
  <p class="front__title">FOUNDER AND CEO</p>

  <ul class="contact">
    <li class="contact__row"><span class="contact__label"><span class="contact__pill">HOME</span></span><span class="contact__value">90071824(5)</span></li>
    <li class="contact__row"><span class="contact__label"><span class="contact__pill">MOBILE</span></span><span class="contact__value">30618475(13)</span></li>
    <li class="contact__row"><span class="contact__label"><span class="contact__pill">EMAIL</span></span><span class="contact__value">martinRD@navora.com</span></li>
    <li class="contact__row"><span class="contact__label"><span class="contact__pill">WEBSITE</span></span><span class="contact__value">www.NAVORA.com</span></li>
  </ul>

  <div class="front__tab"></div>
</section>

<section class="card card--back" aria-label="Business card back">
  <div class="back__bar"></div>
  <p class="tagline tagline--main">you want | we <span class="tagline__accent">trade</span> | you want more</p>
  <p class="tagline tagline--reflection" aria-hidden="true">you want | we <span class="tagline__accent">trade</span> | you want more</p>

  <div class="back__brand">
    <span>NAVORA GENERAL TRADING</span>
    <span class="back__brand-dot"></span>
  </div>

  <div class="back__panel"></div>
</section>

</body>
</html>
```